Overview:
We are seeking a talented graphic designer to create a cinematic and visually captivating movie poster for our upcoming romantic drama, "A Velvet Vow at Solmara". The poster must have a sense of elegance, romance, and the luxurious allure of a Mediterranean escape, while incorporating royal symbolism in a subtle yet sophisticated way.
✨ Design Goals & Style
Theme: Romantic, royal, dreamy, warm, and aspirational.
Setting: Ibiza beach with the sea and sun clearly visible, featuring a warm orange and pink sunset to set the romantic mood.
Colour Palette: Sunset tones – orange, pink, coral, soft golds, and sea blues.
Mood: Glamorous, heartfelt, summery, and regal.
📌 Key Visual Elements
Background:
Ibiza beach scene with sunset (orange & pink tones).
Ocean and horizon line in the distance.
Optionally include subtle silhouettes (e.g., palm trees or a royal yacht far out at sea).
Title Placement:
Movie title “A Velvet Vow at Solmara” should be placed at the top of the poster.
Include lead actor names "Delphine Marsault" and "Jonah Treverstead"
Use an elegant, serif or calligraphic typeface to match the romantic and royal theme.
Title Design Element:
Embed a crown graphic into the title—ideally integrated with one of the letters (like the "R" in "Velvet" or "A") in a tasteful, balanced way.
We'll provide an example image to serve as reference for style.
Also:
A soft glow or lens flare effect from the sunset.
Silhouettes of a couple, subtle and not overpowering.
Space for billing block or release date at the bottom (placeholder text for now).
📎 Deliverables
Final movie poster in vertical format print-ready (CMYK, 300 dpi).
A web-optimized version (RGB, suitable for social media and website use).
Editable source file (Photoshop PSD or Illustrator AI).
Look and feel
Each slider illustrates characteristics of the customer's brand and the style your logo design should communicate.

```html
<!DOCTYPE html>
<html lang="en">
<head>
<meta charset="utf-8">
<title>A Velvet Vow at Solmara — Poster</title>
<link href="https://fonts.googleapis.com/css2?family=Bodoni+Moda:wght@400&family=Montserrat:wght@400;700&display=swap" rel="stylesheet">
<style>
  :root{
    --stage:#2c2c2d;
    --sky-top:#5a284a;
    --sky-plum:#8a3157;
    --sky-rose:#c9455f;
    --sky-coral:#e45a5c;
    --sky-amber:#f08a3a;
    --horizon-gold:#f7a43a;
    --sea-flame:#ea6a26;
    --sea-ember:#d8401f;
    --shore:#b3262a;
    --sand-crimson:#9c1c26;
    --sand-deep:#6e0f1b;
    --credit-orange:#f0955d;
    --title-ivory:#f6efe9;
    --couple-tone:#8a5a78;
  }
  *{box-sizing:border-box;margin:0;padding:0}
  html,body{width:1200px;height:810px;overflow:hidden;background:var(--stage)}
  .stage{width:1200px;height:810px;display:flex;align-items:center;justify-content:center}
  .poster{position:relative;width:533px;height:760px;overflow:hidden}

  .poster__sky{
    position:absolute;left:0;right:0;top:0;height:57.5%;
    background:linear-gradient(180deg,
      var(--sky-top) 0%,
      var(--sky-plum) 30%,
      var(--sky-rose) 55%,
      var(--sky-coral) 72%,
      var(--sky-amber) 90%,
      var(--horizon-gold) 100%);
  }
  .poster__sea{
    position:absolute;left:0;right:0;top:57.5%;height:8%;
    background:linear-gradient(180deg,var(--sea-flame) 0%,var(--sea-ember) 70%,var(--shore) 100%);
  }
  .poster__sand{
    position:absolute;left:0;right:0;top:65.5%;bottom:0;
    background:linear-gradient(180deg,var(--shore) 0%,var(--sand-crimson) 35%,var(--sand-deep) 100%);
  }
  .poster__glow{
    position:absolute;left:50%;top:57.5%;width:260px;height:120px;
    transform:translate(-50%,-50%);
    background:radial-gradient(ellipse at center,rgba(255,210,110,.6),rgba(255,210,110,0) 70%);
  }
  .poster__couple{
    position:absolute;left:147px;top:147px;width:223px;height:345px;
    border-radius:48% 48% 20% 20%;
    background:radial-gradient(ellipse at 50% 40%,rgba(138,90,120,.75),rgba(138,90,120,.35) 60%,rgba(138,90,120,0) 100%);
  }

  .billing{
    position:absolute;top:38px;left:0;right:0;
    display:flex;justify-content:center;align-items:center;gap:14px;
    font-family:'Montserrat',sans-serif;color:var(--credit-orange);
    font-size:10.5px;line-height:1.2;letter-spacing:.02em;text-transform:uppercase;
  }
  .billing__name b{display:block;font-weight:700}
  .billing__name span{display:block;font-weight:400}
  .billing__divider{width:1.5px;height:26px;background:var(--credit-orange)}

  .title{
    position:absolute;left:0;right:0;top:496px;text-align:center;
    font-family:'Bodoni Moda',serif;color:var(--title-ivory);font-weight:400;
  }
  .title__article{display:block;position:relative;font-size:24px;line-height:26px}
  .title__crown{
    position:absolute;left:50%;top:-6px;margin-left:-44px;
    width:20px;height:9px;background:var(--title-ivory);opacity:.85;border-radius:2px;
  }
  .title__line{display:block;font-size:70px;line-height:68px;letter-spacing:-.01em;text-transform:uppercase}
  .title__place{
    display:flex;align-items:center;justify-content:center;gap:10px;margin-top:4px;
    font-family:'Montserrat',sans-serif;font-size:18px;line-height:22px;letter-spacing:.03em;text-transform:uppercase;
  }
  .title__rule{width:120px;height:1px;background:var(--title-ivory);opacity:.8}
</style>
</head>
<body>
<main class="stage">
  <article class="poster">
    <div class="poster__sky" role="img" aria-label="Sunset sky over the sea with a small headland on the left horizon"></div>
    <div class="poster__sea" role="img" aria-label="Calm sea reflecting the setting sun"></div>
    <div class="poster__sand" role="img" aria-label="Rippled red sand beach"></div>
    <div class="poster__glow"></div>
    <div class="poster__couple" role="img" aria-label="Photograph of a smiling couple embracing, fading into the sunset"></div>

    <header class="billing">
      <p class="billing__name"><b>Delphine</b><span>Marsault</span></p>
      <span class="billing__divider"></span>
      <p class="billing__name"><b>Jonah</b><span>Treverstead</span></p>
    </header>

    <h1 class="title">
      <span class="title__article">
        <span class="title__crown" role="img" aria-label="Small crown ornament"></span>A
      </span>
      <span class="title__line">Velvet</span>
      <span class="title__line">Vow</span>
      <span class="title__place">
        <span class="title__rule"></span>At Solmara<span class="title__rule"></span>
      </span>
    </h1>
  </article>
</main>
</body>
</html>
```